Quill And Ferry Business Card

I need a business card designed around my logo (which was designed here on Sketch Forum!)

Target Market(s)

Professional Businesses

Industry/Entity Type

Business

Requirements
Must have
• Details that must be on the business card:

Renata Ovalle
Director
0491 253 608
renata@quillandferry.com.au
www.quillandferry.com.au
PO Box 4720 Marrowby North Vic 3999

```html
<!DOCTYPE html>
<html lang="en">
<head>
<meta charset="utf-8">
<title>Quill And Ferry Business Card</title>
<link rel="stylesheet" href="https://fonts.googleapis.com/css2?family=Cinzel:wght@400&family=Open+Sans:wght@400;700&display=swap">
<style>
  :root {
    --page: #e9e7e4;
    --card-dark: #232323;
    --card-light: #f4f4f4;
    --brand-grey: #a9a9a9;
    --ink: #4a4a4a;
    --accent: #b3121f;
  }
  * { box-sizing: border-box; margin: 0; padding: 0; }
  html, body {
    width: 1200px;
    height: 900px;
    overflow: hidden;
    background: var(--page);
  }
  .stage {
    width: 1200px;
    height: 900px;
    display: flex;
    align-items: center;
    justify-content: center;
    gap: 60px;
  }
  .card {
    position: relative;
    width: 525px;
    height: 300px;
    border-radius: 2px;
    box-shadow: 0 6px 18px rgba(0,0,0,0.18);
  }
  .card--back {
    background: var(--card-dark);
    display: flex;
    align-items: center;
    justify-content: center;
  }
  .card--front {
    background: var(--card-light);
    font-family: "Open Sans", Arial, sans-serif;
    color: var(--ink);
  }
  .brand {
    display: flex;
    align-items: center;
    gap: 14px;
  }
  .brand__mark {
    width: 26px;
    height: 26px;
    background: var(--accent);
  }
  .brand__name {
    font-family: "Cinzel", Georgia, serif;
    font-weight: 400;
    color: var(--brand-grey);
    font-size: 30px;
    letter-spacing: 1px;
    line-height: 1;
    white-space: nowrap;
  }
  .card--front .brand {
    position: absolute;
    top: 44px;
    left: 150px;
  }
  .card--front .brand__mark { width: 20px; height: 20px; }
  .card--front .brand__name { font-size: 22px; }
  .website {
    position: absolute;
    right: 30px;
    top: 128px;
    color: var(--accent);
    font-weight: 700;
    font-size: 14px;
  }
  .contact {
    position: absolute;
    left: 34px;
    bottom: 34px;
  }
  .contact__name {
    font-weight: 700;
    font-size: 19px;
    letter-spacing: 0.5px;
    text-transform: uppercase;
    color: var(--ink);
  }
  .contact__role {
    font-size: 14px;
    margin: 2px 0 12px 22px;
  }
  .contact__list {
    list-style: none;
    font-size: 13.5px;
    line-height: 1.55;
    padding-left: 22px;
  }
  .contact__label {
    display: inline-block;
    width: 14px;
    color: var(--accent);
    font-weight: 700;
  }
</style>
</head>
<body>
  <main class="stage">
    <section class="card card--back" aria-label="Card back">
      <div class="brand">
        <span class="brand__mark"></span>
        <span class="brand__name">Quill And Ferry</span>
      </div>
    </section>

    <section class="card card--front" aria-label="Card front">
      <div class="brand">
        <span class="brand__mark"></span>
        <span class="brand__name">Quill And Ferry</span>
      </div>
      <p class="website">www.quillandferry.com.au</p>
      <div class="contact">
        <h1 class="contact__name">Renata Ovalle</h1>
        <p class="contact__role">Director</p>
        <ul class="contact__list">
          <li><span class="contact__label">t</span>0491 253 608</li>
          <li><span class="contact__label">e</span>renata@quillandferry.com.au</li>
          <li><span class="contact__label"></span>PO Box 4720 Marrowby North Vic 3999</li>
        </ul>
      </div>
    </section>
  </main>
</body>
</html>
```